Global Weight loss program

we need a business card based in Brooklyn , NY called PeppertonRUN . Mara Dulvik Tenbrook the founder and creator of PeppertonRUN Movement. A business based around nutrition, health, Whole Foods and fitness.

Industry/Entity Type

Food Service

Contact Information for Business Card

Phone number : 718-555-0143
website www.peppertonrun.com
email : mara@peppertonrun.com

Font styles to use
Sans Serif

Requirements
Must have
• logo colors
• green black and gold
Nice to have
• must be simple and sharp.
Should not have
• pictures of items

```html
<!DOCTYPE html>
<html lang="en">
<head>
<meta charset="utf-8">
<title>PeppertonRUN Business Card</title>
<link rel="stylesheet" href="https://fonts.googleapis.com/css2?family=Open+Sans:wght@400;600&display=swap">
<style>
  :root {
    --backdrop: #ecebe8;
    --card-light: #ffffff;
    --card-dark: #231f20;
    --ink: #1c1c1c;
    --rule: #3a3a3a;
    --brand-grey: #d6d6d6;
    --brand-green: #6cc04a;
    --tagline: #6a6a6a;
  }
  html, body {
    margin: 0;
    padding: 0;
    width: 1200px;
    height: 900px;
    overflow: hidden;
    background: var(--backdrop);
  }
  .canvas {
    position: relative;
    width: 1200px;
    height: 900px;
    font-family: "Open Sans", Arial, sans-serif;
  }
  .card {
    position: absolute;
    border-radius: 16px;
    box-shadow: 0 6px 18px rgba(0,0,0,0.12);
  }
  .card-front {
    left: 78px;
    top: 35px;
    width: 588px;
    height: 363px;
    background: var(--card-light);
    color: var(--ink);
    text-align: center;
  }
  .holder-name {
    margin: 104px 0 0;
    font-size: 22px;
    font-weight: 600;
    letter-spacing: 0.5px;
  }
  .holder-role {
    margin: 4px 0 0;
    font-size: 15px;
    font-weight: 400;
    letter-spacing: 0.5px;
  }
  .divider {
    width: 188px;
    height: 1px;
    margin: 16px auto 17px;
    background: var(--rule);
  }
  .contact-list {
    list-style: none;
    margin: 0;
    padding: 0;
    font-size: 15px;
    line-height: 24.5px;
    letter-spacing: 0.3px;
  }
  .card-back {
    left: 390px;
    top: 507px;
    width: 565px;
    height: 348px;
    background: var(--card-dark);
    text-align: center;
  }
  .brand-square {
    display: block;
    width: 44px;
    height: 44px;
    margin: 96px auto 0;
    background: var(--brand-green);
  }
  .brand-name {
    margin: 28px 0 0;
    font-size: 40px;
    font-weight: 600;
    line-height: 1;
    color: var(--brand-grey);
  }
  .brand-tagline {
    margin: 6px 0 0;
    font-size: 10px;
    letter-spacing: 1.4px;
    color: var(--tagline);
  }
</style>
</head>
<body>
<main class="canvas">
  <section class="card card-front">
    <h1 class="holder-name">MARA DULVIK TENBROOK</h1>
    <p class="holder-role">FOUNDER</p>
    <div class="divider"></div>
    <ul class="contact-list">
      <li>718-555-0143</li>
      <li>MARA@PEPPERTONRUN.COM</li>
      <li>WWW.PEPPERTONRUN.COM</li>
    </ul>
  </section>
  <section class="card card-back">
    <span class="brand-square"></span>
    <p class="brand-name">PeppertonRUN</p>
    <p class="brand-tagline">Fitness, Nutrition and Health</p>
  </section>
</main>
</body>
</html>
```